Kestrel Vitality a Centre Pty Ltd

Business card is to promote and represent our new business. It's situated in
47 Fenwick Road
Brookvale 2100 Sydney
Our clinic is all about getting people back to great health giving them back their lifestyle in half the usual time it takes to get results elsewhere , we do this through innovative therapies with latest state of the art equipment ,skills ,knowledge and experience.
We give them back their pain free healthy lifestyle with lots of energy to love life and perform their best Quickly and effectively .
The final design should communicate
Trust , confidence, results .
Updates

Reason: Waiting for some designers to submit work Thanks

Target Market(s)

High end clients that take their health and results seriously ,
High end athletes , as well as general people that want to see results with different
Treatment Methods and approach

Industry/Entity Type

Clinic

Contact Information for Business Card

Kestrel Vitality Centre Pty Ltd
47 Fenwick Road Brookvale 2100 Sydney
Website www.kestrelvitalitycentre.com.au

Font styles to use
Other font styles liked:
• Gothic font medium

Requirements
Must have
• A designe that makes people look twice with a wow factor , a designe that isn't like all the rest .
• Must have the logo in the colours Iv provided in my files
• Must communicate Trust, confidence , results
Nice to have
• 1) The logo raised up or
• 2) Maybe a pop up logo on the card ?
• Or let's be creative and have two cards one on top of the other so the two cards slide .... The front will have the kestrel logo with the address details etc
• The other card with have
• eg your next app .......................................repeating all way down the card
Should not have
• Basic plain looking card that everyone else has

```html
<!DOCTYPE html>
<html lang="en">
<head>
<meta charset="utf-8">
<title>Kestrel Vitality Centre – Business Card</title>
<link href="https://fonts.googleapis.com/css2?family=Open+Sans:wght@400;600;700&display=swap" rel="stylesheet">
<style>
  :root {
    --backdrop: #dcdcdc;
    --navy: #2b2e72;
    --navy-deep: #2a2a63;
    --sky: #4a90cf;
    --green: #2a9a3c;
    --green-dark: #1f7d32;
    --text-grey: #555a66;
    --white: #ffffff;
  }
  * { margin: 0; padding: 0; box-sizing: border-box; }
  html, body {
    width: 1200px; height: 840px; overflow: hidden;
    background: var(--backdrop);
    font-family: "Open Sans", Arial, sans-serif;
  }
  .canvas { position: relative; width: 1200px; height: 840px; }

  .card { position: absolute; top: 275px; height: 265px; overflow: hidden; }

  /* Front */
  .card-front {
    left: 95px; width: 436px;
    background: linear-gradient(180deg, var(--navy-deep) 0%, #3a63a8 35%, var(--sky) 50%, #3a62a6 72%, var(--navy) 100%);
  }
  .front-emblem-area {
    position: absolute; left: 200px; top: 0; width: 240px; height: 265px;
    background: radial-gradient(ellipse at 60% 45%, rgba(120,180,200,0.22), rgba(120,180,200,0) 65%);
  }
  .front-brand {
    position: absolute; left: 33px; top: 160px;
    display: flex; align-items: center; gap: 10px;
  }
  .brand-dot { width: 14px; height: 14px; border-radius: 50%; background: var(--white); }
  .front-brand .brand-name {
    color: var(--white); font-weight: 700; font-size: 24px; letter-spacing: 0.2px;
  }

  /* Back */
  .card-back { left: 633px; width: 465px; background: var(--white); }
  .back-emblem-area {
    position: absolute; right: 0; top: 0; width: 220px; height: 240px;
    background: radial-gradient(ellipse at 60% 55%, rgba(200,210,200,0.28), rgba(255,255,255,0) 65%);
  }
  .back-brand {
    position: absolute; left: 25px; top: 58px;
    display: flex; align-items: center; gap: 9px;
  }
  .back-brand .brand-dot { background: var(--green); }
  .back-brand .brand-name { color: var(--navy); font-weight: 700; font-size: 22px; }

  .name-tab {
    position: absolute; left: 0; top: 133px; width: 7px; height: 35px;
    background: linear-gradient(180deg, var(--sky), var(--navy));
    border-radius: 0 3px 3px 0;
  }
  .person { position: absolute; left: 25px; top: 133px; }
  .person-name { color: var(--navy); font-weight: 700; font-size: 16px; line-height: 20px; }
  .person-role { color: var(--text-grey); font-size: 11px; line-height: 14px; }

  .address {
    position: absolute; left: 25px; top: 184px;
    font-size: 11px; line-height: 15px; color: var(--text-grey);
  }
  .address .company { color: var(--navy); font-weight: 700; }

  .contacts {
    position: absolute; left: 225px; top: 184px; list-style: none;
    font-size: 11px; line-height: 15px; color: var(--text-grey);
  }
  .contacts li { display: flex; align-items: center; gap: 5px; }
  .contacts svg { width: 10px; height: 10px; fill: var(--navy); flex: none; }

  .footer-band { position: absolute; left: 0; bottom: 0; width: 465px; height: 25px; }
  .band-green {
    position: absolute; left: 0; top: 4px; width: 205px; height: 21px;
    background: linear-gradient(90deg, var(--green-dark), var(--green));
    clip-path: polygon(0 0, 100% 0, 96% 100%, 0 100%);
  }
  .band-blue {
    position: absolute; left: 200px; top: 0; width: 265px; height: 25px;
    background: linear-gradient(90deg, var(--sky), var(--navy) 55%);
    clip-path: polygon(4% 0, 100% 0, 100% 100%, 0 100%);
  }
  .website {
    position: absolute; right: 12px; top: 4px;
    color: var(--white); font-size: 11px; line-height: 17px;
  }
</style>
</head>
<body>
<main class="canvas">

  <section class="card card-front" aria-label="Card front">
    <div class="front-emblem-area" role="img" aria-label="Faint brand emblem decoration"></div>
    <div class="front-brand">
      <span class="brand-dot"></span>
      <span class="brand-name">Kestrel Vitality Centre</span>
    </div>
  </section>

  <section class="card card-back" aria-label="Card back">
    <div class="back-emblem-area" role="img" aria-label="Faint brand emblem decoration"></div>

    <div class="back-brand">
      <span class="brand-dot"></span>
      <span class="brand-name">Kestrel Vitality Centre</span>
    </div>

    <div class="name-tab"></div>
    <div class="person">
      <p class="person-name">Daniel Harwick</p>
      <p class="person-role">Director</p>
    </div>

    <address class="address" style="font-style:normal">
      <span class="company">Kestrel Vitality Centre</span><br>
      Pty Ltd 47 Fenwick Road Brookvale<br>
      2100 Sydney Website
    </address>

    <ul class="contacts">
      <li>
        <svg viewBox="0 0 24 24" aria-hidden="true"><path d="M6.6 10.8a15.1 15.1 0 0 0 6.6 6.6l2.2-2.2a1 1 0 0 1 1-.25 11.4 11.4 0 0 0 3.6.57 1 1 0 0 1 1 1V20a1 1 0 0 1-1 1A17 17 0 0 1 3 4a1 1 0 0 1 1-1h3.5a1 1 0 0 1 1 1c0 1.25.2 2.45.57 3.6a1 1 0 0 1-.25 1z"/></svg>
        +61 2 5550 1834
      </li>
      <li>
        <svg viewBox="0 0 24 24" aria-hidden="true"><path d="M7 1h10a2 2 0 0 1 2 2v18a2 2 0 0 1-2 2H7a2 2 0 0 1-2-2V3a2 2 0 0 1 2-2zm0 3v14h10V4zm5 15.5a1 1 0 1 0 0 2 1 1 0 0 0 0-2z"/></svg>
        0400 555 018
      </li>
      <li>
        <svg viewBox="0 0 24 24" aria-hidden="true"><path d="M2 5h20v14H2zm2 2v.5l8 5 8-5V7zm0 3v7h16v-7l-8 5z"/></svg>
        daniel@kestrelvitalitycentre.com.au
      </li>
    </ul>

    <div class="footer-band">
      <div class="band-green"></div>
      <div class="band-blue"></div>
      <span class="website">www.kestrelvitalitycentre.com.au</span>
    </div>
  </section>

</main>
</body>
</html>
```